Theo Brandvik Photography
Theo Brandvik Photography's Homepage
Photography
Professional photographer
top
Overall look and feel should come from logo design.

```html
<!DOCTYPE html>
<html lang="en">
<head>
<meta charset="utf-8">
<title>Theo Brandvik Photography</title>
<link rel="stylesheet" href="https://fonts.googleapis.com/css2?family=Federo&family=Arimo:wght@400&display=swap">
<style>
  :root {
    --page: #000000;
    --band-top: #2a2a2a;
    --band-bottom: #0a0a0a;
    --ink: #ffffff;
    --ink-soft: #d8d8d8;
    --muted: #9a9a9a;
    --accent: #c0202a;
    --rule: #333333;
    --logo-bg: #ffffff;
    --logo-ink: #111111;
  }
  * { margin: 0; padding: 0; box-sizing: border-box; }
  html, body { width: 1200px; height: 897px; overflow: hidden; background: var(--page); }
  .page {
    position: relative; width: 1200px; height: 897px;
    background: linear-gradient(to bottom, var(--band-top) 0, var(--band-bottom) 182px, var(--page) 182px);
    font-family: "Arimo", Arial, sans-serif; color: var(--ink);
  }
  .brand {
    position: absolute; left: 444px; top: 12px; width: 261px; height: 61px;
    background: var(--logo-bg); display: flex; align-items: center; justify-content: center; gap: 10px;
  }
  .brand-mark { width: 30px; height: 30px; background: var(--logo-ink); }
  .brand-name { font-family: "Federo", sans-serif; font-size: 22px; color: var(--logo-ink); letter-spacing: 0.5px; }
  .nav-accent { position: absolute; left: 140px; top: 96px; width: 90px; height: 4px; background: var(--accent); }
  .main-nav, .nav-reflection {
    position: absolute; left: 133px; width: 962px; display: flex; justify-content: space-between;
    font-family: "Federo", sans-serif; font-size: 41px; list-style: none;
  }
  .main-nav { top: 100px; }
  .nav-reflection { top: 142px; transform: scaleY(-0.5); opacity: 0.12; pointer-events: none; }
  .about-title { position: absolute; left: 138px; top: 205px; font-family: "Federo", sans-serif; font-size: 40px; font-weight: 400; }
  .about-copy { position: absolute; left: 65px; top: 286px; width: 350px; font-size: 13.5px; line-height: 16.8px; color: var(--ink-soft); }
  .about-copy p { margin-bottom: 17px; }
  .feature-photo {
    position: absolute; left: 439px; top: 213px; width: 700px; height: 483px;
    border: 8px solid var(--ink);
    background: radial-gradient(ellipse at 60% 50%, #c98a4c 0, #8a7a6a 18%, #dcdcdc 38%, #f2f2f2 70%, #e6e6e6 100%);
  }
  .thumbs { position: absolute; left: 439px; top: 705px; width: 700px; display: flex; justify-content: space-between; }
  .thumb { width: 136px; height: 102px; border: 4px solid var(--ink); }
  .t1 { background: linear-gradient(135deg, #e8e8e8, #c8854a 50%, #f0f0f0); }
  .t2 { background: linear-gradient(135deg, #6a8a2a, #c89a3a 50%, #3a5a1a); }
  .t3 { background: linear-gradient(135deg, #c0301a, #7aa0c8 50%, #a0201a); }
  .t4 { background: linear-gradient(135deg, #c8d0d8, #5a7aa8 50%, #dde2e8); }
  .t5 { background: linear-gradient(135deg, #f0f0f0, #c8804a 50%, #e4e4e4); }
  .footer-rule { position: absolute; left: 0; top: 831px; width: 1200px; height: 1px; background: var(--rule); }
  .footer-divider { position: absolute; left: 504px; top: 838px; width: 1px; height: 22px; background: var(--rule); }
  .footer-nav { position: absolute; left: 61px; top: 841px; display: flex; gap: 14px; list-style: none; font-size: 12px; color: var(--ink-soft); }
  .footer-brand {
    position: absolute; left: 965px; top: 836px; width: 174px; height: 44px;
    background: var(--logo-bg); display: flex; align-items: center; justify-content: center; gap: 6px;
  }
  .footer-brand .brand-mark { width: 18px; height: 18px; }
  .footer-brand .brand-name { font-size: 13px; }
</style>
</head>
<body>
<div class="page">
  <header>
    <div class="brand"><span class="brand-mark"></span><span class="brand-name">Theo Brandvik Photography</span></div>
    <div class="nav-accent"></div>
    <ul class="main-nav">
      <li>Home</li><li>Portfolio</li><li>About</li><li>Clients Area</li><li>Links</li><li>Contact</li>
    </ul>
    <ul class="nav-reflection" aria-hidden="true">
      <li>Home</li><li>Portfolio</li><li>About</li><li>Clients Area</li><li>Links</li><li>Contact</li>
    </ul>
  </header>
  <main>
    <h1 class="about-title">About Us</h1>
    <div class="about-copy">
      <p>Lorem ipsum dolor sit amet, consectetur adipiscing elit. Pellentesque luctus viverra tortor nec vulputate. Proin a hendrerit turpis. Pellentesque placerat, lacus nec ultrices cursus, ipsum ante sollicitudin diam, nec feugiat tortor magna eu velit. Integer risus mi, vulputate in ultrices ut, hendrerit vitae justo. Donec nec lacus. Donec quis ligula odio, eu luctus odio.</p>
      <p>Sed blandit porttitor erat vel auctor. Praesent quis est enim. Praesent vel orci eu neque lacinia lacinia. Suspendisse pretium elit eu lorem bibendum commodo. Maecenas dictum ante a justo viverra dictum. Vestibulum sed nisl vitae diam elementum venenatis. Suspendisse a tellus, nec condimentum odio. Curabitur eu lacus quis felis adipiscing.</p>
      <p>Vivamus adipiscing rutrum vulputate. Nam blandit viverra velit, vel gestas tortor blandit eu. Curabitur velit lectus, imperdiet eu fermentum in, porttitor sit amet neque.</p>
    </div>
    <div class="feature-photo" role="img" aria-label="Photograph of a robin perched on a snowy branch with red berries"></div>
    <div class="thumbs">
      <div class="thumb t1" role="img" aria-label="Thumbnail photo of a robin in snow"></div>
      <div class="thumb t2" role="img" aria-label="Thumbnail photo of a hummingbird among leaves"></div>
      <div class="thumb t3" role="img" aria-label="Thumbnail photo of a small blue bird on a red background"></div>
      <div class="thumb t4" role="img" aria-label="Thumbnail photo of a bird with blue feathers"></div>
      <div class="thumb t5" role="img" aria-label="Thumbnail photo of a robin on a branch"></div>
    </div>
  </main>
  <footer>
    <div class="footer-rule"></div>
    <ul class="footer-nav">
      <li>Home</li><li>Portfolio</li><li>About</li><li>Clients Area</li><li>Links</li><li>Contact</li>
    </ul>
    <div class="footer-divider"></div>
    <div class="footer-brand"><span class="brand-mark"></span><span class="brand-name">Theo Brandvik Photography</span></div>
  </footer>
</div>
</body>
</html>
```